Retail Jewelry Business Card Design Project

We are in need of a new business card design for a retail jewelry store. This store is in the business of fine jewelry including but not specific to bridal jewelry, diamonds, designer jewelry and watches.

This store has been in business for 20 years but continues to strive for a modern professional appeal. The main colors use for this business are a royal blue, white and silver.

Target Market(s)

Target market is ages 18-50

Industry/Entity Type

Jewelry

Requirements
Must have
• Sales Person Name
Sales Person Email Address

Store Address
Store Phone
Website

Standard business card size. No odd shapes or sizes.
Nice to have
• Overall modern feel for card.

We have thought that a design with a nice feature of the logo on the back of the card would be nice but open to ideas.
Should not have
• No specific images of jewelry should be used.

```html
<!DOCTYPE html>
<html lang="en">
<head>
<meta charset="utf-8">
<title>Marlowe Reed Fine Jewelry — Business Card</title>
<link rel="stylesheet" href="https://fonts.googleapis.com/css2?family=Alegreya:wght@400;700&display=swap">
<style>
  :root {
    --page: #e9e6e1;
    --navy-top: #0f2949;
    --navy-bottom: #27506f;
    --gold: #d9ae3f;
    --ink-light: #f2f4f7;
    --shadow: rgba(0, 0, 0, 0.28);
  }
  * { margin: 0; padding: 0; box-sizing: border-box; }
  html, body {
    width: 1200px;
    height: 1000px;
    overflow: hidden;
    background: var(--page);
  }
  .canvas {
    position: relative;
    width: 1200px;
    height: 1000px;
  }
  .card {
    position: absolute;
    left: 250px;
    width: 700px;
    height: 400px;
    background: linear-gradient(180deg, var(--navy-top) 0%, var(--navy-bottom) 100%);
    box-shadow: 0 10px 26px var(--shadow);
    font-family: "Alegreya", Georgia, serif;
  }
  .card--back { top: 70px; }
  .card--front { top: 530px; }

  .brand-name {
    color: var(--gold);
    font-weight: 700;
    line-height: 1.05;
  }
  .card--back .brand-name {
    position: absolute;
    left: 60px;
    top: 48px;
    font-size: 30px;
  }
  .brand-name .brand-line {
    display: block;
  }
  .card--back .brand-line--sub {
    font-size: 15px;
    letter-spacing: 3px;
    margin-top: 4px;
    padding-left: 28px;
  }

  .contact {
    position: absolute;
    right: 46px;
    bottom: 40px;
    text-align: right;
    color: var(--ink-light);
    font-size: 17px;
    line-height: 1.45;
  }
  .contact__block + .contact__block { margin-top: 16px; }

  .card--front .brand-name {
    position: absolute;
    left: 0;
    right: 0;
    top: 120px;
    text-align: center;
    font-size: 74px;
  }
  .card--front .brand-line--sub {
    font-size: 30px;
    letter-spacing: 8px;
    margin-top: 10px;
  }
</style>
</head>
<body>
<main class="canvas">
  <section class="card card--back" aria-label="Card back with contact details">
    <div class="brand-name">
      <span class="brand-line">Marlowe Reed</span>
      <span class="brand-line brand-line--sub">FINE JEWELRY</span>
    </div>
    <address class="contact" style="font-style: normal;">
      <div class="contact__block">
        2280 Linden Avenue<br>
        Harbor City, FL 32000
      </div>
      <div class="contact__block">tel: (555) 214 - 0386</div>
      <div class="contact__block">
        www.marlowereedjewelry.com<br>
        mail: mara@marlowereedjewelry.com
      </div>
    </address>
  </section>

  <section class="card card--front" aria-label="Card front with store name">
    <div class="brand-name">
      <span class="brand-line">Marlowe Reed</span>
      <span class="brand-line brand-line--sub">FINE JEWELRY</span>
    </div>
  </section>
</main>
</body>
</html>
```